Graphic Design Set for Banner Ads - Sizes and Specs for Bidlane

We need a set of 6 ads of the following sizes created for Bidlane:

Medium rectangle: 300×250
Leaderboard: 728×90
Wide skyscraper: 160×600
Large rectangle: 300x600
Mobile leaderboard: 320×50

Here are the Formatting Guidelines (WEB ADS): https://help.bidlane.com/hc/en-us/articles/583920147-Ad-Content-and-Format-Guidelines

Here is the website: https://mavenhollowcare.com/

Here are some words for the ad - feel free to use creative liberties if you have something better or need less words.

1. The Future of Aging is Here

2. Dementia At-Home Care

3. Benefits of an Assisted Living from the Privacy of Your Home - link to

4. Idaho's New Senior Care Option

5. The Security of Senior Living from the Comfort of Your Home

I have the images for all website photos, if you need more images, please let me know.

Target Market(s)

Women age 55+

Industry/Entity Type

Graphic Design

Requirements
Must have
• Incorporate website imagery as much as possible
Should not have
• a feeling of helplessness, old, etc.

```html
<!DOCTYPE html>
<html lang="en">
<head>
<meta charset="utf-8">
<title>Maven Hollow – Banner Ad Set</title>
<link rel="stylesheet" href="https://fonts.googleapis.com/css2?family=Roboto:wght@400;500&display=swap">
<style>
  :root {
    --gold: #b78f30;
    --gold-deep: #a98328;
    --ink: #4a3410;
    --ink-dark: #2b2111;
    --paper: #f2f2f2;
    --stage: #ece8e3;
    --photo-a: #6f8a4c;
    --photo-b: #a89a86;
    --photo-c: #d9d4cb;
  }
  * { box-sizing: border-box; margin: 0; padding: 0; }
  html, body { width: 1200px; height: 1075px; overflow: hidden; }
  body {
    position: relative;
    background: var(--stage);
    font-family: "Roboto", Arial, sans-serif;
    color: var(--ink);
  }
  .ad {
    position: absolute;
    overflow: hidden;
    background: var(--gold);
    box-shadow: 0 3px 8px rgba(0,0,0,.18);
    display: flex;
  }
  .ad--vertical { flex-direction: column; }
  .photo {
    background: linear-gradient(160deg, var(--photo-a) 0%, var(--photo-b) 55%, var(--photo-c) 100%);
    flex: none;
  }
  .message {
    position: relative;
    flex: none;
    display: flex;
    flex-direction: column;
    align-items: center;
    justify-content: center;
    text-align: center;
    color: var(--ink-dark);
  }
  .headline { font-weight: 400; line-height: 1.2; }
  .headline strong { font-weight: 500; color: var(--ink); display: block; }
  .cta {
    display: inline-block;
    border: 2px solid var(--ink);
    color: var(--ink-dark);
    font-weight: 400;
    letter-spacing: .04em;
    text-transform: uppercase;
    text-decoration: none;
    text-align: center;
    white-space: nowrap;
  }
  .brand {
    position: relative;
    flex: 1;
    min-width: 0;
    background: var(--paper);
    display: flex;
    align-items: center;
    justify-content: center;
    gap: 8px;
  }
  .brand-name {
    font-weight: 400;
    color: var(--ink-dark);
    letter-spacing: .04em;
    text-transform: uppercase;
    white-space: nowrap;
  }
  .brand-dot {
    width: 12px; height: 12px; border-radius: 50%;
    background: var(--gold);
    flex: none;
  }
  .brand--curved::before {
    content: "";
    position: absolute;
    left: -10%; right: -10%; top: -14px;
    height: 40px;
    border-radius: 50%;
    background: var(--paper);
  }
  .brand--curved > * { position: relative; }

  /* Leaderboard 728×90 */
  .leaderboard { left: 78px; top: 76px; width: 908px; height: 112px; }
  .leaderboard .photo { width: 198px; }
  .leaderboard .message { width: 550px; flex-direction: row; gap: 36px; }
  .leaderboard .headline { font-size: 32px; }
  .leaderboard .cta { font-size: 16px; padding: 7px 20px; }
  .leaderboard .brand { gap: 6px; padding: 0 6px; }
  .leaderboard .brand-name { font-size: 16px; letter-spacing: .02em; }
  .leaderboard .brand-dot { width: 9px; height: 9px; }

  /* Large rectangle 300×600 */
  .large-rectangle { left: 78px; top: 240px; width: 373px; height: 748px; }
  .large-rectangle .photo { height: 366px; }
  .large-rectangle .message { height: 288px; gap: 46px; padding-bottom: 20px; }
  .large-rectangle .headline { font-size: 36px; }
  .large-rectangle .cta { font-size: 17px; padding: 12px 32px; }
  .large-rectangle .brand-name { font-size: 26px; }

  /* Wide skyscraper 160×600 */
  .skyscraper { left: 500px; top: 240px; width: 200px; height: 748px; }
  .skyscraper .photo { height: 248px; }
  .skyscraper .message { height: 350px; gap: 46px; padding: 0 12px 56px; }
  .skyscraper .headline { font-size: 28px; line-height: 1.4; }
  .skyscraper .cta { font-size: 16px; padding: 8px 18px; }
  .skyscraper .brand { flex-direction: column; gap: 6px; padding-bottom: 20px; }
  .skyscraper .brand-name { font-size: 19px; }

  /* Medium rectangle 300×250 */
  .medium-rectangle { left: 750px; top: 240px; width: 375px; height: 310px; }
  .medium-rectangle .photo { height: 188px; }
  .medium-rectangle .message { height: 60px; }
  .medium-rectangle .headline { font-size: 23px; }
  .medium-rectangle .headline strong { display: inline; }
  .medium-rectangle .brand { justify-content: space-between; padding: 0 22px; }
  .medium-rectangle .brand-name { font-size: 20px; }
  .medium-rectangle .cta { font-size: 16px; padding: 6px 20px; border-color: var(--gold); }

  /* Mobile leaderboard 320×50 */
  .mobile-leaderboard { left: 750px; top: 603px; width: 400px; height: 60px; }
  .mobile-leaderboard .photo { width: 78px; }
  .mobile-leaderboard .message { width: 235px; gap: 5px; }
  .mobile-leaderboard .headline { font-size: 13px; }
  .mobile-leaderboard .headline strong { display: inline; font-weight: 400; color: var(--ink-dark); }
  .mobile-leaderboard .cta { font-size: 10px; padding: 2px 12px; }
  .mobile-leaderboard .brand { flex-direction: column; gap: 2px; }
  .mobile-leaderboard .brand-name { font-size: 10px; letter-spacing: .01em; }
  .mobile-leaderboard .brand-dot { width: 6px; height: 6px; }
</style>
</head>
<body>

  <section class="ad leaderboard" aria-label="Leaderboard 728 by 90">
    <div class="photo" role="img" aria-label="Photo of a smiling senior woman seated in a garden chair beside a white curly-coated dog"></div>
    <div class="message">
      <h2 class="headline">Idaho's New<strong>Senior Care Option</strong></h2>
      <a class="cta" href="https://mavenhollowcare.com/">Learn More</a>
    </div>
    <div class="brand"><span class="brand-dot"></span><span class="brand-name">Maven Hollow</span></div>
  </section>

  <section class="ad ad--vertical large-rectangle" aria-label="Large rectangle 300 by 600">
    <div class="photo" role="img" aria-label="Photo of a smiling senior woman seated in a garden chair beside a white curly-coated dog"></div>
    <div class="message">
      <h2 class="headline">Idaho's New<strong>Senior Care Option</strong></h2>
      <a class="cta" href="https://mavenhollowcare.com/">Learn More</a>
    </div>
    <div class="brand brand--curved"><span class="brand-dot"></span><span class="brand-name">Maven Hollow</span></div>
  </section>

  <section class="ad ad--vertical skyscraper" aria-label="Wide skyscraper 160 by 600">
    <div class="photo" role="img" aria-label="Photo of a smiling senior woman seated in a garden chair beside a white curly-coated dog"></div>
    <div class="message">
      <h2 class="headline">Idaho's New<strong>Senior Care Option</strong></h2>
      <a class="cta" href="https://mavenhollowcare.com/">Learn More</a>
    </div>
    <div class="brand brand--curved"><span class="brand-dot"></span><span class="brand-name">Maven Hollow</span></div>
  </section>

  <section class="ad ad--vertical medium-rectangle" aria-label="Medium rectangle 300 by 250">
    <div class="photo" role="img" aria-label="Photo of a smiling senior woman seated in a garden chair beside a white curly-coated dog"></div>
    <div class="message">
      <h2 class="headline">Idaho's New <strong>Senior Care Option</strong></h2>
    </div>
    <div class="brand">
      <span class="brand-name">Maven Hollow</span>
      <a class="cta" href="https://mavenhollowcare.com/">Learn More</a>
    </div>
  </section>

  <section class="ad mobile-leaderboard" aria-label="Mobile leaderboard 320 by 50">
    <div class="photo" role="img" aria-label="Photo of a smiling senior woman seated in a garden chair beside a white curly-coated dog"></div>
    <div class="message">
      <h2 class="headline">Idaho's New <strong>Senior Care Option</strong></h2>
      <a class="cta" href="https://mavenhollowcare.com/">Learn More</a>
    </div>
    <div class="brand"><span class="brand-dot"></span><span class="brand-name">Maven Hollow</span></div>
  </section>

</body>
</html>
```